Website Page Re-Design

I have 2 pages that need to be re-designed on my site. This is the site so you can take a look and get a feel for the layout etc, www.vortaplay.com
I have included screen shots of the individual pages I want redone as well as some examples from other sites for ideas.

Homepage Story, would like the redo sunday file, to be made stunning, only the content, picture and share buttons need be altered the, would like and emphasis on intergrating the share buttons, the story page starts here http://www.vortaplay.com/league/ball-hockey/mens/news-division/ so what is beingcreated is when the read more is clicked

Free Agent Forms:
Needs to be re-worked so that there isn't so much white space on the page.

Industry/Entity Type

News

Requirements
Must have
• share buttons to slick very well intergrated
Nice to have
• Share buttons to be top notch

```html
<!DOCTYPE html>
<html lang="en">
<head>
<meta charset="utf-8">
<title>VortaPlay – Men's Ball Hockey Free Agent Registration</title>
<link href="https://fonts.googleapis.com/css2?family=Nunito:ital,wght@0,400;0,600;0,700;0,800;0,900;1,600&family=Open+Sans:wght@400;600&display=swap" rel="stylesheet">
<style>
  :root {
    --field-green: #7eb13a;
    --field-green-dark: #6a9c2c;
    --panel: #e7f2d9;
    --ink: #4a4a4a;
    --label-green: #5b8d1f;
    --accent-green: #6aa52a;
    --nav-yellow: #f4f07a;
    --brush: #141414;
    --white: #ffffff;
    --input-bg: #f1f3f6;
    --input-border: #c8ccd2;
    --placeholder: #8a8f99;
    --share-blue: #3d5f9e;
    --post-blue: #2ea6d8;
    --email-blue: #4d8fcf;
    --plus-grey: #e9e9e9;
    --comment-green: #4f9a1c;
  }
  * { box-sizing: border-box; margin: 0; padding: 0; }
  html, body { width: 1200px; height: 750px; overflow: hidden; }
  body {
    position: relative;
    font-family: "Nunito", sans-serif;
    background: radial-gradient(ellipse at 50% 20%, #9cc75a 0%, var(--field-green) 45%, var(--field-green-dark) 100%);
  }
  .brand {
    position: absolute; left: 202px; top: 18px;
    font-family: "Nunito", sans-serif; font-weight: 800; font-size: 40px;
    color: var(--white); letter-spacing: -1px;
  }
  .top-nav {
    position: absolute; left: 648px; top: 0; width: 353px; height: 23px;
    background: var(--nav-yellow); border-radius: 0 0 6px 6px;
    display: flex; align-items: center; justify-content: space-around;
    font-family: "Open Sans", sans-serif; font-size: 12px; color: #222;
  }
  .top-nav span + span { border-left: 1px solid #b8a44a; padding-left: 9px; }
  .main-nav {
    position: absolute; left: 524px; top: 34px; width: 476px; height: 42px;
    background: var(--brush); border-radius: 14px 4px 16px 6px;
    display: flex; align-items: center; justify-content: flex-end; gap: 0; padding-right: 20px;
  }
  .main-nav a {
    color: var(--white); font-style: italic; font-weight: 600; font-size: 13px;
    text-decoration: underline; padding: 0 10px;
  }
  .main-nav a + a { border-left: 1px solid #777; }
  .panel {
    position: absolute; left: 200px; top: 88px; width: 802px; height: 578px;
    background: var(--panel); border-radius: 8px;
  }
  .banner {
    position: absolute; left: 14px; top: 11px; width: 775px; height: 92px;
    background: linear-gradient(90deg, #3f7d18 0%, #6ba532 60%, #8dbf4e 100%);
    border-radius: 3px;
  }
  .banner-players {
    position: absolute; left: 14px; top: -10px; width: 540px; height: 102px;
    background: linear-gradient(180deg, #c89a78 0%, #b4463a 65%, #d84a2a 100%);
    border-radius: 40px 40px 0 0;
  }
  .follow-card {
    position: absolute; left: 594px; top: 19px; width: 140px; height: 54px;
    background: #000; border-radius: 5px;
    display: flex; align-items: center; gap: 10px; padding-left: 13px;
    color: var(--white); font-size: 13px; font-weight: 600; line-height: 13px;
  }
  .follow-card i { width: 28px; height: 28px; background: #3b5c9b; border-radius: 4px; display: block; }
  .page-title {
    position: absolute; left: 32px; top: 134px; font-weight: 800; font-size: 25px;
    letter-spacing: -1.2px; line-height: 26px; color: var(--ink);
  }
  .page-title strong { display: block; color: var(--accent-green); font-weight: 900; }
  .share { position: absolute; top: 138px; }
  .share .count {
    width: 44px; height: 24px; background: #fff; border: 1px solid #d4dbe3; border-radius: 2px;
    font-family: "Open Sans", sans-serif; font-size: 10px; text-align: center; line-height: 22px; color: #333;
  }
  .share .btn {
    margin-top: 7px; width: 44px; height: 16px; border-radius: 2px;
    font-family: "Open Sans", sans-serif; font-size: 8.5px; font-weight: 600; color: #fff;
    display: flex; align-items: center; justify-content: center; gap: 3px;
  }
  .share .btn i { width: 6px; height: 6px; background: #fff; display: block; }
  .field-label { position: absolute; font-weight: 700; font-size: 11.5px; color: var(--label-green); letter-spacing: -0.3px; line-height: 12px; }
  .input {
    position: absolute; height: 25px; background: var(--input-bg); border: 1px solid var(--input-border);
    border-radius: 3px; font-style: italic; font-size: 9px; color: var(--placeholder);
    padding-left: 16px; line-height: 23px;
  }
  .select-arrow { position: absolute; right: -1px; top: -1px; width: 25px; height: 25px; background: #4d9d20; border-radius: 0 3px 3px 0; }
  .rule { position: absolute; border-top: 2px dotted #b9d59a; }
  .group-title { position: absolute; top: 394px; font-weight: 800; font-size: 14.5px; letter-spacing: -0.7px; color: var(--label-green); }
  .group-title small { font-weight: 400; font-size: 7px; color: #7fae48; letter-spacing: 0; }
  .option { position: absolute; font-size: 12px; color: #6c8e46; display: flex; align-items: center; gap: 8px; }
  .option i { width: 11px; height: 11px; border: 1px solid #c3c9cf; background: #fff; display: block; }
  .action {
    position: absolute; top: 516px; height: 24px; border-radius: 3px;
    font-weight: 800; font-size: 9.5px; display: flex; align-items: center; justify-content: center;
  }
  .submit { left: 30px; width: 65px; background: linear-gradient(#5cb338, #3a8e1d); color: #fff; }
  .reset { left: 98px; width: 65px; background: #fff; border: 1px solid #c8c8c8; color: #4a7d1e; }
  .legal {
    position: absolute; left: 200px; top: 701px; font-family: "Open Sans", sans-serif;
    font-size: 8.5px; letter-spacing: 0.8px; color: var(--white);
  }
</style>
</head>
<body>
  <div class="brand">VortaPlay</div>
  <nav class="top-nav"><span>Home</span><span>About Us</span><span>FAQS</span><span>Contact Us</span><span>Jobs</span></nav>
  <nav class="main-nav"><a>Leagues</a><a>Schedules &amp; More</a><a>Register</a><a>Pay</a><a>Forum</a><a>Sponsors</a></nav>

  <main class="panel">
    <div class="banner">
      <div class="banner-players" role="img" aria-label="Row of league players in hockey jerseys and caps"></div>
      <div class="follow-card"><i></i><span>Find Us On<br>Chatterly</span></div>
    </div>

    <h1 class="page-title">Men’s Ball Hockey Free Agent<strong>Registration.</strong></h1>

    <div class="share" style="left:544px"><div class="count">11</div><div class="btn" style="background:var(--share-blue)"><i></i>share</div></div>
    <div class="share" style="left:592px"><div class="count" style="color:#2a8bc4">10</div><div class="btn" style="background:var(--post-blue)"><i></i>post</div></div>
    <div class="share" style="left:640px"><div class="count" style="font-size:12px">2</div><div class="btn" style="background:var(--plus-grey);color:#d04030;border:1px solid #ccc"><i style="background:#d04030"></i>+1</div></div>
    <div class="share" style="left:682px"><div class="count">3</div><div class="btn" style="background:var(--email-blue)"><i></i>email</div></div>
    <div class="share" style="left:730px"><div class="count">6</div><div class="btn" style="background:var(--comment-green)">comment</div></div>

    <div class="field-label" style="left:29px;top:220px">Men’s Ball Hockey Free Agent<br>First Name</div>
    <div class="input" style="left:28px;top:250px;width:168px">∗ Required</div>
    <div class="field-label" style="left:224px;top:232px">Last Name</div>
    <div class="input" style="left:222px;top:250px;width:169px">∗ Required</div>

    <div class="field-label" style="left:28px;top:296px">Email Address</div>
    <div class="input" style="left:28px;top:313px;width:168px">∗ Required</div>
    <div class="field-label" style="left:224px;top:297px">Cell Phone</div>
    <div class="input" style="left:222px;top:313px;width:169px">∗ Required</div>
    <div class="field-label" style="left:414px;top:297px">Gender</div>
    <div class="input" style="left:414px;top:313px;width:89px;padding-left:9px">∗ Required<span class="select-arrow"></span></div>

    <div class="rule" style="left:28px;top:363px;width:748px"></div>

    <div class="group-title" style="left:28px">Preferred Position <small>(*Required)</small></div>
    <div class="option" style="left:30px;top:423px"><i></i>Forward</div>
    <div class="option" style="left:30px;top:445px"><i></i>Defense</div>
    <div class="option" style="left:30px;top:467px"><i></i>Goalie</div>

    <div class="group-title" style="left:224px">Skill Level <small>(*Required)</small></div>
    <div class="option" style="left:226px;top:424px"><i></i>Bigner</div>
    <div class="option" style="left:226px;top:446px"><i></i>Average</div>
    <div class="option" style="left:226px;top:468px"><i></i>All-Star</div>

    <div class="group-title" style="left:416px">How should Teams Contact You <small>(*Required)</small></div>
    <div class="option" style="left:416px;top:424px"><i></i>Text Msg</div>
    <div class="option" style="left:416px;top:446px"><i></i>Call Me</div>
    <div class="option" style="left:416px;top:468px"><i></i>E-mail</div>

    <div class="action submit">SUBMIT</div>
    <div class="action reset">RESET</div>
    <div class="rule" style="left:174px;top:527px;width:602px"></div>
  </main>

  <footer class="legal">© 2011, VORTAPLAY. ALL RIGHTS RESERVED.</footer>
</body>
</html>
```